Project Managers Business card design

We need business cards for our Project Managers based in Sydney for our business name Korbet Pty Ltd. We project manage property improvements and infrastructure Assets. We provide asset owners Project Management services from original concept, management of architectural and engineering designs, call and select construction tenders, and manage the Asset operational life cycle to conclusion and removal. We are experienced in feasibility studies, risk assessments, quality control, safety control, environmental analysis. We are specialist in Aged Care and Child Care Services. We can provide asset reviewing checklists, asset inspections, contract cost and contract assessments, dispute resolution services and articles and books on safely working and living in environments subject to analysis. the design colours should be queensland marone and NSW sky blue.

Industry/Entity Type

Construction

Contact Information for Business Card

Gavin Trelowe (Mb 0412 847 391), Dennis Marquay (Mb 0438 216 074), Luke Benhadda,(Mb 0421 963 158)
E: all business cards: korbet@fernmail.example
Office phone number (02) 9482 3165
Address
Level 1 Halyard House
47 Wexford Lane, Parramatta
Web: projectmanagers@worksleadsbykorbet.example (to be checked on Printlyne web draft)

```html
<!DOCTYPE html>
<html lang="en">
<head>
<meta charset="utf-8">
<title>Korbet Pty Ltd – Gavin Trelowe business card</title>
<link rel="stylesheet" href="https://fonts.googleapis.com/css2?family=Inter:ital,wght@0,600;0,700;1,600&display=swap">
<style>
  :root {
    --maroon: #86263a;
    --maroon-deep: #781d35;
    --white: #ffffff;
    --portrait-light: #c9c6c2;
    --portrait-mid: #9b9691;
  }
  * { box-sizing: border-box; margin: 0; padding: 0; }
  html, body { width: 1200px; height: 741px; overflow: hidden; background: var(--white); }
  body { font-family: "Inter", Arial, sans-serif; }

  .card {
    position: relative;
    width: 1200px;
    height: 741px;
    overflow: hidden;
    background: linear-gradient(120deg, var(--maroon) 0%, var(--maroon-deep) 100%);
    color: var(--white);
  }

  .portrait-ring {
    position: absolute;
    left: 75px; top: 61px;
    width: 204px; height: 204px;
    border: 2px dashed var(--white);
    border-radius: 50%;
  }
  .portrait {
    position: absolute;
    left: 10px; top: 10px;
    width: 180px; height: 180px;
    border-radius: 50%;
    background: radial-gradient(circle at 50% 40%, var(--portrait-light) 0%, var(--portrait-mid) 100%);
  }

  .person { position: absolute; left: 77px; top: 287px; }
  .person-name { font-size: 39px; font-weight: 700; letter-spacing: 0.5px; line-height: 1.1; }
  .person-role { font-size: 22px; font-weight: 600; font-style: italic; margin-top: 2px; }

  .brand {
    position: absolute;
    right: 76px; top: 126px;
    font-size: 58px; font-weight: 700; letter-spacing: 1px;
    line-height: 1;
  }

  .contact-tag {
    position: absolute;
    top: 511px;
    height: 50px;
    padding: 0 16px;
    border: 2px dashed var(--white);
    display: flex; align-items: center; justify-content: center;
    font-size: 20px; font-weight: 600; white-space: nowrap;
    transform: translateX(-50%);
  }
  .tag-phone { left: 158px; width: 228px; }
  .tag-web   { left: 600px; }
  .tag-email { left: 1020px; }

  .info-band {
    position: absolute;
    left: 0; top: 616px;
    width: 1200px; height: 115px;
    background: var(--white);
  }
  .pointer {
    position: absolute;
    top: -24px;
    width: 0; height: 0;
    border-left: 14px solid transparent;
    border-right: 14px solid transparent;
    border-bottom: 24px solid var(--white);
    transform: translateX(-50%);
  }
  .icon {
    position: absolute;
    top: 42px;
    width: 40px; height: 40px;
    transform: translateX(-50%);
    fill: var(--maroon-deep);
  }
  .at-phone { left: 158px; }
  .at-web   { left: 600px; }
  .at-email { left: 1020px; }

  .base-strip {
    position: absolute;
    left: 0; bottom: 0;
    width: 1200px; height: 10px;
    background: var(--maroon-deep);
  }
</style>
</head>
<body>
<div class="card">
  <div class="portrait-ring">
    <div class="portrait" role="img" aria-label="Portrait photo of Gavin Trelowe"></div>
  </div>

  <div class="person">
    <div class="person-name">Gavin Trelowe</div>
    <div class="person-role">Project Manager</div>
  </div>

  <div class="brand">KORBET</div>

  <div class="contact-tag tag-phone">0412 847 391</div>
  <div class="contact-tag tag-web">www.assetmanagementbykorbet.example</div>
  <div class="contact-tag tag-email">korbet@fernmail.example</div>

  <div class="info-band">
    <span class="pointer at-phone"></span>
    <span class="pointer at-web"></span>
    <span class="pointer at-email"></span>

    <svg class="icon at-phone" viewBox="0 0 24 24" aria-label="Phone">
      <path d="M6.6 10.8c1.4 2.8 3.8 5.1 6.6 6.6l2.2-2.2c.3-.3.7-.4 1-.2 1.1.4 2.3.6 3.6.6.6 0 1 .4 1 1V20c0 .6-.4 1-1 1C10.6 21 3 13.4 3 4c0-.6.4-1 1-1h3.5c.6 0 1 .4 1 1 0 1.3.2 2.5.6 3.6.1.3 0 .7-.2 1l-2.3 2.2z"/>
    </svg>

    <svg class="icon at-web" viewBox="0 0 24 24" aria-label="Website">
      <circle cx="12" cy="12" r="10"/>
      <g fill="none" stroke="#ffffff" stroke-width="1.4">
        <ellipse cx="12" cy="12" rx="4.2" ry="10"/>
        <line x1="2" y1="12" x2="22" y2="12"/>
        <path d="M4 6.5h16M4 17.5h16"/>
      </g>
    </svg>

    <svg class="icon at-email" viewBox="0 0 24 24" aria-label="Email">
      <path d="M3 5h18c.6 0 1 .4 1 1v.6l-10 6.2L2 6.6V6c0-.6.4-1 1-1z"/>
      <path d="M2 8.9l10 6.2 10-6.2V18c0 .6-.4 1-1 1H3c-.6 0-1-.4-1-1V8.9z"/>
    </svg>
  </div>

  <div class="base-strip"></div>
</div>
</body>
</html>
```